Copper Lantern Coffee Bean Labels

We need a label for a new brand of coffee that we are selling in Portland, Oregon (Coffee Capital). Our company has no current online presence but have some great roasting techniques. We will be roasting our own coffee beans from throughout the world and selling them immediately after roasting causing a super fresh and high quality product.

We will be packaging in brown kraft bags: 3 3/8 X 2.5 x 7.75 inches which is standard for coffee beans.

Also notice on that sample the blue section in the middle has the product name. We want to also make it so that there is a consistent area that we can print OVER the label the name or blend of the coffee.

Our company is called Copper Lantern Coffee Roasters. We will want to put copperlanternroasters.example on the label someplace (we dont have a site yet but will by launch).

We need to incorporate A Black Diamond into the design. No preferences yet on the style of it.

We want to be a super-premium brand. Sort of like MicroBrew beers. We will sell at Farmers Markets, online, and directly into stores. Image is very important to us.

Labels should be about 3" wide and about 3.75" high.. Perhaps higher if a cool design justifies the height. Again we will be using a brown kraft bag (like grocery bag color) as shown on the sample.

SEE ATTACHED SEVERAL INTERESTING DESIGNS

Target Market(s)

Foodies, Yuppie, Coffee Snob

Industry/Entity Type

It Company

Requirements
Must have
• Location for the product Name to go onto it... We want to use the same labels for our full line. Just printing over it something like "Italian Roast" and a line below saying something like "Bold, Nutty Flavor, blah blah"

Should not have
• Clunkey looking old fonts or things that look homemade.

```html
<!DOCTYPE html>
<html lang="en">
<head>
<meta charset="utf-8">
<title>Copper Lantern Coffee Bean Labels</title>
<link href="https://fonts.googleapis.com/css2?family=Fjalla+One&family=Great+Vibes&family=Arimo:wght@400;700&display=swap" rel="stylesheet">
<style>
  :root {
    --backdrop: #efe9e1;
    --espresso: #2e1d14;
    --roast: #4a2c1a;
    --mocha: #6b3f22;
    --cream: #e7d7b5;
    --cream-deep: #cbb48a;
    --copper: #b9823f;
    --gold: #d7a75a;
    --white: #f7f3ec;
    --ink: #2a1a10;
  }
  * { box-sizing: border-box; margin: 0; padding: 0; }
  html, body { width: 1200px; height: 1003px; overflow: hidden; }
  body { background: var(--backdrop); position: relative; font-family: "Arimo", Arial, sans-serif; }

  .label { position: absolute; overflow: hidden; box-shadow: 0 3px 10px rgba(0,0,0,.25); }

  /* ---------- Label A : bean-pattern badge ---------- */
  .label-badge { left: 160px; top: 320px; width: 236px; height: 350px; background: var(--mocha); }
  .label-badge .bean-field { position: absolute; inset: 0;
    background: radial-gradient(circle at 50% 50%, #74442a 0%, var(--roast) 75%); }
  .label-badge .title-panel { position: absolute; left: 45px; top: 0; width: 150px; height: 150px;
    background: repeating-linear-gradient(90deg, var(--cream) 0 6px, #ddc9a2 6px 12px); text-align: center; }
  .fresh { font-family: "Fjalla One", "Arial Narrow", sans-serif; color: var(--ink); letter-spacing: .2px; }
  .coffee-script { font-family: "Great Vibes", cursive; color: var(--ink); }
  .label-badge .fresh { font-size: 19px; padding-top: 8px; line-height: 1; }
  .label-badge .coffee-script { font-size: 30px; line-height: .8; margin-top: -2px; }
  .name-band { background: var(--roast); color: var(--white); font-weight: 700; text-align: center; }
  .label-badge .name-band { position: absolute; left: 55px; top: 60px; width: 130px; height: 24px; font-size: 15px; line-height: 24px;
    box-shadow: 0 0 0 2px var(--cream-deep); }
  .flavor { font-family: "Great Vibes", cursive; color: var(--ink); }
  .label-badge .flavor { position: absolute; left: 45px; top: 87px; width: 150px; text-align: center; font-size: 15px; }
  .label-badge .badge { position: absolute; left: 50px; top: 118px; width: 136px; height: 136px; border-radius: 50%;
    background: var(--espresso); box-shadow: 0 0 0 3px var(--copper); display: flex; align-items: center; justify-content: center; }
  .label-badge .badge-inner { width: 104px; height: 104px; border-radius: 50%; background: var(--white);
    display: flex; align-items: center; justify-content: center; text-align: center;
    font-size: 11px; font-weight: 700; color: var(--roast); line-height: 1.25; padding: 8px; }
  .label-badge .pennant { position: absolute; left: 58px; top: 240px; }
  .label-badge .site { position: absolute; right: -68px; top: 250px; transform: rotate(-90deg);
    font-size: 6px; color: var(--cream); width: 150px; text-align: center; }

  /* ---------- Label B : framed cup ---------- */
  .label-frame { left: 640px; top: 307px; width: 240px; height: 346px;
    background: repeating-linear-gradient(90deg, #3b2a20 0 14px, #33241b 14px 28px); }
  .label-frame .frame-art { position: absolute; inset: 0; }
  .label-frame .maker { position: absolute; left: 0; top: 88px; width: 240px; text-align: center;
    font-size: 8px; font-weight: 700; color: var(--white); }
  .label-frame .maker-site { position: absolute; left: 0; top: 100px; width: 240px; text-align: center; font-size: 5px; color: var(--cream); }
  .label-frame .fresh { position: absolute; left: 0; top: 113px; width: 240px; text-align: center; font-size: 22px; color: var(--cream); line-height: 1; }
  .label-frame .coffee-script { position: absolute; left: 0; top: 130px; width: 240px; text-align: center; font-size: 34px; color: var(--cream); line-height: 1; }
  .label-frame .name-band { position: absolute; left: 60px; top: 177px; width: 120px; height: 22px; font-size: 14px; line-height: 22px;
    background: var(--cream); color: var(--ink); box-shadow: 0 0 0 2px var(--copper); }
  .label-frame .flavor { position: absolute; left: 0; top: 202px; width: 240px; text-align: center; font-size: 11px; color: var(--gold); }
</style>
</head>
<body>

  <!-- Label A -->
  <section class="label label-badge">
    <div class="bean-field" role="img" aria-label="Pattern of outlined coffee beans on dark brown"></div>
    <div class="title-panel">
      <p class="fresh">Fresh Roasted</p>
      <p class="coffee-script">Coffee</p>
    </div>
    <p class="name-band">Italian Roast</p>
    <p class="flavor">Bold, Nutty Flavor</p>
    <svg class="pennant" width="120" height="105" viewBox="0 0 120 105">
      <path d="M0 0 H120 V80 L60 105 L0 80 Z" fill="#2e1d14"/>
      <path d="M38 20 H82 V78 L60 88 L38 78 Z" fill="#b9823f"/>
      <circle cx="60" cy="62" r="12" fill="#2e1d14" stroke="#d7a75a" stroke-width="2"/>
    </svg>
    <div class="badge"><div class="badge-inner">Copper Lantern Coffee Roasters</div></div>
    <p class="site">www.copperlanternroasters.example</p>
  </section>

  <!-- Label B -->
  <section class="label label-frame">
    <svg class="frame-art" width="240" height="346" viewBox="0 0 240 346">
      <defs>
        <linearGradient id="beanTone" x1="0" y1="0" x2="0" y2="1">
          <stop offset="0" stop-color="#6b3f22"/><stop offset="1" stop-color="#2e1d14"/>
        </linearGradient>
      </defs>
      <path d="M40 12 Q120 -6 200 12 V70 H40 Z" fill="url(#beanTone)" stroke="#b9823f" stroke-width="2" role="img" aria-label="Roasted coffee beans"/>
      <path d="M38 60 H202 L218 76 V300 L202 318 H38 L22 300 V76 Z" fill="#2e1d14" stroke="#b9823f" stroke-width="3"/>
      <path d="M45 68 H195 L210 80 V296 L195 310 H45 L30 296 V80 Z" fill="none" stroke="#d7a75a" stroke-width="1"/>
      <path d="M0 172 H22 V210 H0 Z M218 172 H240 V210 H218 Z" fill="#2e1d14"/>
      <path d="M50 318 Q120 346 190 318 V336 H50 Z" fill="url(#beanTone)" stroke="#b9823f" stroke-width="2" role="img" aria-label="Roasted coffee beans"/>
      <rect x="78" y="232" width="84" height="72" rx="36" fill="#e7d7b5" opacity=".9" role="img" aria-label="Steaming cup of coffee on a saucer"/>
    </svg>
    <p class="maker">Copper Lantern Coffee Roasters</p>
    <p class="maker-site">www.copperlanternroasters.example</p>
    <p class="fresh">Fresh Roasted</p>
    <p class="coffee-script">Coffee</p>
    <p class="name-band">Italian Roast</p>
    <p class="flavor">Bold, Nutty Flavor</p>
  </section>

</body>
</html>
```